We need a flyer design to promote Penhallow & Tibbs Landscaping and Lawn Maintenance.

The flyer needs to be have:-
1) A great head line ( When quality matters)
2) A really awesome offer ( no obligation free trial mow)
3) A sense of scarcity (Due to time restraints, we can only take limited number of free lawn jobs. This offer is only available to the first 20 callers)
4) A call to action (Call now to avoid disappointment)
5) Contact details (Penhallow & Tibbs Landscaping and Lawn Maintenance 0452 786 305)

The layout of the entire flyer should come across to potential customers as

1) simple to understand what Penhallow & Tibbs offer (not overcrowd with messages; the main aim is to communicate across our services.)

The list of services that Penhallow & Tibbs provide will be:-

- Lawn Mowing - Pruning - Weeding
- Mulching - Edging - Hedging
- Trimming - Fertilising - Garden maintenance
- Weekly, fortnightly or monthly programs

Thank you.

```html
<!DOCTYPE html>
<html lang="en">
<head>
<meta charset="utf-8">
<title>Penhallow &amp; Tibbs Landscaping and Lawn Maintenance</title>
<link rel="stylesheet" href="https://fonts.googleapis.com/css2?family=Marcellus+SC&family=Yanone+Kaffeesatz:wght@400;700&family=Mulish:ital,wght@1,400;1,800&family=Nunito:wght@800;900&family=Questrial&display=swap">
<style>
  :root {
    --brown: #4a2c10;
    --green: #5db33f;
    --green-dark: #3e9a2f;
    --band: #b9dca0;
    --band-soft: rgba(205, 232, 190, 0.6);
    --lawn-1: #3f9a23;
    --lawn-2: #62c436;
    --white: #ffffff;
    --grey-shape: rgba(140, 140, 140, 0.42);
  }
  * { margin: 0; padding: 0; box-sizing: border-box; }
  html, body { width: 846px; height: 1200px; overflow: hidden; background: var(--white); }
  .flyer { position: relative; width: 846px; height: 1200px; overflow: hidden; background: var(--white); }

  .hero {
    position: absolute; left: 0; top: 0; width: 846px; height: 520px;
    background:
      radial-gradient(ellipse 22% 9% at 8% 28%, rgba(232, 120, 170, 0.85), transparent 70%),
      radial-gradient(ellipse 16% 8% at 22% 4%, rgba(240, 180, 50, 0.85), transparent 70%),
      radial-gradient(ellipse 18% 6% at 45% 5%, rgba(215, 60, 80, 0.8), transparent 70%),
      radial-gradient(ellipse 15% 6% at 62% 3%, rgba(245, 150, 60, 0.8), transparent 70%),
      radial-gradient(ellipse 18% 5% at 85% 3%, rgba(200, 90, 160, 0.8), transparent 70%),
      radial-gradient(ellipse 20% 12% at 14% 14%, rgba(60, 130, 40, 0.95), transparent 75%),
      radial-gradient(ellipse 120% 38% at 85% 40%, rgba(120, 215, 80, 0.55), transparent 70%),
      linear-gradient(170deg, #4f8e2c 0%, #5aa833 9%, var(--lawn-2) 20%, #55b52d 55%, var(--lawn-1) 100%);
  }
  .brand-band {
    position: absolute; left: 0; top: 195px; width: 846px; height: 130px;
    background: var(--band-soft); text-align: center;
  }
  .brand-name {
    font-family: "Marcellus SC", serif; font-weight: 400; color: var(--brown);
    font-size: 46px; line-height: 1; margin-top: 14px; letter-spacing: 1px;
  }
  .brand-trade {
    font-family: "Questrial", sans-serif; color: var(--green);
    font-size: 22px; letter-spacing: 30px; margin-top: 7px; padding-left: 30px;
  }
  .brand-sub {
    font-family: "Marcellus SC", serif; color: var(--brown);
    font-size: 23px; margin-top: 9px;
  }

  .mower-shape {
    position: absolute; left: 250px; top: 520px; width: 600px; height: 680px;
    background:
      radial-gradient(ellipse 38% 30% at 38% 68%, var(--grey-shape), transparent 72%),
      radial-gradient(ellipse 12% 40% at 80% 30%, rgba(140, 140, 140, 0.25), transparent 72%);
  }

  .headline-band {
    position: absolute; left: 0; top: 520px; width: 846px; height: 56px;
    background: var(--band); text-align: center;
    font-family: "Yanone Kaffeesatz", sans-serif; font-weight: 400; font-size: 48px; line-height: 56px;
    color: var(--brown);
  }

  .gallery { position: absolute; left: 0; top: 576px; width: 846px; height: 186px; background: var(--green-dark); }
  .gallery-photo { position: absolute; top: 3px; height: 180px; }
  .photo-mower {
    left: 3px; width: 205px;
    background:
      radial-gradient(ellipse 45% 25% at 30% 85%, rgba(235, 235, 235, 0.9), transparent 70%),
      radial-gradient(ellipse 55% 35% at 45% 30%, #d8262c, transparent 75%),
      linear-gradient(160deg, #6f8e45 0%, #5a7f34 60%, #4d7430 100%);
  }
  .photo-path {
    left: 214px; width: 208px;
    background:
      radial-gradient(ellipse 40% 30% at 35% 80%, #b3614a, transparent 75%),
      radial-gradient(ellipse 30% 30% at 15% 20%, #d2303a, transparent 75%),
      radial-gradient(ellipse 35% 25% at 75% 25%, #d8c040, transparent 75%),
      radial-gradient(ellipse 50% 30% at 85% 85%, #5cb83a, transparent 75%),
      linear-gradient(180deg, #8a7a5a 0%, #6f8a3a 100%);
  }
  .photo-hand {
    left: 427px; width: 207px;
    background:
      radial-gradient(ellipse 45% 14% at 55% 55%, #c88c6c, transparent 75%),
      linear-gradient(180deg, #1f4a12 0%, #3f8a22 40%, #55a82c 100%);
  }
  .photo-flowers {
    left: 639px; width: 207px;
    background:
      radial-gradient(ellipse 60% 22% at 60% 60%, #e2bce0, transparent 75%),
      radial-gradient(ellipse 30% 15% at 40% 15%, #d04a5a, transparent 75%),
      linear-gradient(180deg, #4f8a30 0%, #6cae3c 50%, #5aa532 100%);
  }

  .offer {
    position: absolute; left: 0; top: 768px; width: 846px; text-align: center;
    font-family: "Mulish", sans-serif; font-style: italic; font-size: 22.5px; line-height: 30px;
    letter-spacing: 0.45px; color: #111;
  }
  .offer strong { color: var(--green); font-weight: 800; }

  .services-band {
    position: absolute; left: 0; top: 865px; width: 846px; height: 38px;
    background: var(--band); text-align: center;
    font-family: "Nunito", sans-serif; font-weight: 900; font-size: 23px; line-height: 38px;
    color: var(--brown);
  }
  .services-list { position: absolute; top: 913px; list-style: none; }
  .services-left { left: 205px; }
  .services-right { left: 414px; }
  .services-list li {
    position: relative; padding-left: 34px; height: 32.5px;
    font-family: "Questrial", sans-serif; font-size: 22px; letter-spacing: 0.6px;
    line-height: 30px; color: var(--brown);
  }
  .services-list li.two-line { height: auto; line-height: 27px; }
  .services-list svg { position: absolute; left: 0; top: 5px; width: 21px; height: 21px; }

  .cta-band {
    position: absolute; left: 0; top: 1102px; width: 846px; height: 98px;
    background: var(--band); text-align: center;
  }
  .cta-line {
    font-family: "Yanone Kaffeesatz", sans-serif; font-weight: 700;
    font-size: 42px; letter-spacing: 0.5px; color: var(--green); margin-top: 2px; line-height: 46px;
    transform: skewX(-10deg);
  }
  .cta-phone {
    font-family: "Nunito", sans-serif; font-weight: 900; font-size: 34px;
    color: var(--brown); letter-spacing: 1.5px; line-height: 44px;
  }
</style>
</head>
<body>
<main class="flyer">
  <div class="hero" role="img" aria-label="Photo of a freshly mown lawn curving past colourful flower beds"></div>
  <header class="brand-band">
    <h1 class="brand-name">Penhallow &amp; Tibbs</h1>
    <div class="brand-trade">LANDSCAPING</div>
    <div class="brand-sub">and Lawn Maintenance</div>
  </header>

  <div class="mower-shape" role="img" aria-label="Faint grey silhouette of a lawn mower in the background"></div>

  <h2 class="headline-band">When quality matters...</h2>

  <section class="gallery">
    <div class="gallery-photo photo-mower" role="img" aria-label="Red lawn mower on grass"></div>
    <div class="gallery-photo photo-path" role="img" aria-label="Brick garden path with steps and flowering plants"></div>
    <div class="gallery-photo photo-hand" role="img" aria-label="Hand resting on soft green lawn"></div>
    <div class="gallery-photo photo-flowers" role="img" aria-label="Curved flower bed of pink blooms beside a lawn"></div>
  </section>

  <p class="offer">No obligation free trail mow!<br>Due to time restraints, we can only take a limited number of free<br>lawn jobs. This offer is only available to the first <strong>20</strong> callers!</p>

  <h3 class="services-band">Services</h3>

  <ul class="services-list services-left">
    <li><svg viewBox="0 0 22 22"><circle cx="11" cy="11" r="9.5" fill="none" stroke="var(--green)" stroke-width="2"/><path d="M9 7l4 4-4 4" fill="none" stroke="var(--green)" stroke-width="2.2" stroke-linecap="round" stroke-linejoin="round"/></svg>Lawn Mowing</li>
    <li><svg viewBox="0 0 22 22"><circle cx="11" cy="11" r="9.5" fill="none" stroke="var(--green)" stroke-width="2"/><path d="M9 7l4 4-4 4" fill="none" stroke="var(--green)" stroke-width="2.2" stroke-linecap="round" stroke-linejoin="round"/></svg>Pruning</li>
    <li><svg viewBox="0 0 22 22"><circle cx="11" cy="11" r="9.5" fill="none" stroke="var(--green)" stroke-width="2"/><path d="M9 7l4 4-4 4" fill="none" stroke="var(--green)" stroke-width="2.2" stroke-linecap="round" stroke-linejoin="round"/></svg>Weeding</li>
    <li><svg viewBox="0 0 22 22"><circle cx="11" cy="11" r="9.5" fill="none" stroke="var(--green)" stroke-width="2"/><path d="M9 7l4 4-4 4" fill="none" stroke="var(--green)" stroke-width="2.2" stroke-linecap="round" stroke-linejoin="round"/></svg>Mulching</li>
    <li><svg viewBox="0 0 22 22"><circle cx="11" cy="11" r="9.5" fill="none" stroke="var(--green)" stroke-width="2"/><path d="M9 7l4 4-4 4" fill="none" stroke="var(--green)" stroke-width="2.2" stroke-linecap="round" stroke-linejoin="round"/></svg>Edging</li>
  </ul>
  <ul class="services-list services-right">
    <li><svg viewBox="0 0 22 22"><circle cx="11" cy="11" r="9.5" fill="none" stroke="var(--green)" stroke-width="2"/><path d="M9 7l4 4-4 4" fill="none" stroke="var(--green)" stroke-width="2.2" stroke-linecap="round" stroke-linejoin="round"/></svg>Hedging</li>
    <li><svg viewBox="0 0 22 22"><circle cx="11" cy="11" r="9.5" fill="none" stroke="var(--green)" stroke-width="2"/><path d="M9 7l4 4-4 4" fill="none" stroke="var(--green)" stroke-width="2.2" stroke-linecap="round" stroke-linejoin="round"/></svg>Trimming</li>
    <li><svg viewBox="0 0 22 22"><circle cx="11" cy="11" r="9.5" fill="none" stroke="var(--green)" stroke-width="2"/><path d="M9 7l4 4-4 4" fill="none" stroke="var(--green)" stroke-width="2.2" stroke-linecap="round" stroke-linejoin="round"/></svg>Fertilizing</li>
    <li><svg viewBox="0 0 22 22"><circle cx="11" cy="11" r="9.5" fill="none" stroke="var(--green)" stroke-width="2"/><path d="M9 7l4 4-4 4" fill="none" stroke="var(--green)" stroke-width="2.2" stroke-linecap="round" stroke-linejoin="round"/></svg>Garden maintenance</li>
    <li class="two-line"><svg viewBox="0 0 22 22"><circle cx="11" cy="11" r="9.5" fill="none" stroke="var(--green)" stroke-width="2"/><path d="M9 7l4 4-4 4" fill="none" stroke="var(--green)" stroke-width="2.2" stroke-linecap="round" stroke-linejoin="round"/></svg>Weekly, fortnightly or<br>monthly programs</li>
  </ul>

  <footer class="cta-band">
    <div class="cta-line">CALL NOW TO AVOID DISAPPOINTMENT</div>
    <div class="cta-phone">0452 786 305</div>
  </footer>
</main>
</body>
</html>
```